Horse related business entrepreneur needs a business card

I need a business card design for my horse related business. The enterprise is Copper Vale LLC and I have 3 businesses (headquartered at 2 locations): 1. property management where we rent horse stalls and apartments at a thoroughbred training center outside Ocala; 2. a medium sized transportation service in central Florida that sells horse bedding and removes used horse bedding from horse farms; and horse racing

```html
<!DOCTYPE html>
<html lang="en">
<head>
<meta charset="utf-8">
<title>Copper Vale LLC — Business Card</title>
<link rel="stylesheet" href="https://fonts.googleapis.com/css2?family=Montserrat:wght@400;700;800&family=Open+Sans:wght@400;600&display=swap">
<style>
  :root {
    --bg: #2a2a2c;
    --card-dark-1: #2b2d30;
    --card-dark-2: #121314;
    --orange: #e8603a;
    --orange-deep: #c94a26;
    --orange-mid: #d9542f;
    --white: #ffffff;
    --muted: #b9b9b9;
    --ink: #0b0b0b;
    --photo-1: #5a5a5c;
    --photo-2: #2b2b2d;
  }
  * { margin: 0; padding: 0; box-sizing: border-box; }
  html, body { width: 1200px; height: 900px; overflow: hidden; background: var(--bg); }
  .stage { position: relative; width: 1200px; height: 900px; }

  .card {
    position: absolute;
    width: 560px; height: 320px;
    border-radius: 26px;
    overflow: hidden;
    box-shadow: 0 18px 40px rgba(0,0,0,.45);
  }

  /* Back card */
  .card-back {
    left: 60px; top: 100px;
    background: radial-gradient(ellipse at 55% 35%, var(--card-dark-1), var(--card-dark-2) 85%);
    color: var(--white);
    font-family: "Open Sans", sans-serif;
  }
  .company {
    position: absolute; left: 0; right: 0; top: 104px;
    text-align: center;
    font-family: "Montserrat", sans-serif;
    font-weight: 800; font-size: 46px; letter-spacing: 1px;
  }
  .company .suffix { font-weight: 700; font-size: 26px; margin-left: 6px; }
  .addresses {
    position: absolute; left: 40px; right: 30px; bottom: 40px;
    display: flex; align-items: center; gap: 22px;
    font-size: 15px; line-height: 1.15;
  }
  .mark { width: 34px; height: 34px; border-radius: 50%; background: var(--orange); flex: none; }
  .divider { width: 2px; height: 52px; background: var(--orange); margin-bottom: 20px; align-self: flex-end; }
  .address-secondary { align-self: flex-start; margin-top: -40px; }

  /* Front card */
  .card-front { left: 580px; top: 480px; background: var(--orange); }
  .photo {
    position: absolute; left: 0; top: 0; bottom: 0; width: 280px;
    background: radial-gradient(ellipse at 55% 40%, var(--photo-1), var(--photo-2) 90%);
  }
  .layers { position: absolute; inset: 0; }
  .name-band {
    position: absolute; left: 230px; right: 0; top: 100px; height: 58px;
    background: var(--ink);
    border-radius: 29px 0 0 29px;
    text-align: right; padding: 6px 26px 0 0;
  }
  .person {
    font-family: "Montserrat", sans-serif; color: var(--white);
    font-size: 26px; line-height: 1; letter-spacing: .5px;
  }
  .person .first { font-weight: 800; }
  .person .last { font-weight: 400; }
  .role {
    font-family: "Montserrat", sans-serif; font-weight: 700;
    font-size: 14px; color: var(--muted); letter-spacing: 1px; margin-top: 3px;
  }
  .contacts {
    position: absolute; right: 14px; top: 176px;
    font-family: "Open Sans", sans-serif; color: var(--white);
    font-size: 17px;
  }
  .contact-row {
    display: flex; justify-content: flex-end; align-items: center;
    height: 30px; border-bottom: 1px solid rgba(255,255,255,.35);
  }
  .contact-row:last-child { border-bottom: none; }
  .contact-row .value { padding-right: 10px; }
  .contact-row .key {
    width: 24px; height: 30px; line-height: 30px; text-align: center;
    border-left: 1px solid rgba(255,255,255,.7);
    color: var(--ink); font-weight: 600;
  }
</style>
</head>
<body>
<main class="stage">

  <section class="card card-back">
    <h1 class="company">COPPER VALE<span class="suffix">LLC</span></h1>
    <div class="addresses">
      <span class="mark" aria-hidden="true"></span>
      <address class="address-primary">1270 SE 96th Lane<br>Fairfield, FL 32634</address>
      <span class="divider" aria-hidden="true"></span>
      <address class="address-secondary">5182 Willow Ridge Road<br>Afton, VA 22920</address>
    </div>
  </section>

  <section class="card card-front">
    <div class="photo" role="img" aria-label="Photograph of a dark bay horse galloping on a grey backdrop"></div>
    <svg class="layers" width="560" height="320" viewBox="0 0 560 320" aria-hidden="true">
      <polygon points="240,0 290,0 330,320 280,320" fill="var(--orange-deep)"/>
      <polygon points="262,0 310,0 355,320 305,320" fill="var(--orange-mid)"/>
      <polygon points="286,0 340,0 380,320 330,320" fill="#e2592f"/>
      <polygon points="312,0 560,0 560,320 355,320" fill="var(--orange)"/>
      <polygon points="312,0 330,0 372,320 355,320" fill="rgba(0,0,0,.12)"/>
    </svg>
    <div class="name-band">
      <p class="person"><span class="first">DANE</span> <span class="last">WHITLOW</span></p>
      <p class="role">OWNER</p>
    </div>
    <div class="contacts">
      <p class="contact-row"><span class="value">(555) 210-4837</span><span class="key">P</span></p>
      <p class="contact-row"><span class="value">(555) 318-6624</span><span class="key">F</span></p>
      <p class="contact-row"><span class="value">dane@coppervale.com</span><span class="key">E</span></p>
    </div>
  </section>

</main>
</body>
</html>
```